Contemporary Elegant Business Card Design for an International Trade Company in the Wine Industry

We need a new business card design for an international trade company in the wine and winemaking industry. The overall feel of the card should be contemporary, upscale, luxurious and elegant. It should communicate confidence and professionalism. The colors should complementary to our logo design (burgundy, gold, and black).
Inspiration: rich velvet tapestry
The card should include the following information:
Business: Brovenna Trading/Shipping, LLC.
Name: Marcus T. Hollenbrand
Title: CEO
Email: mark@brovennatrading.example
Phone: 555-294-6172
www.brovennatrading.example
Updates
Project Deadline Extended
Reason: We'd like the designers that we requested some additional designs from to still submit designs. Thank you!
Industry/Entity Type
Business
Contact Information for Business Card
Title: CEO
Phone: 555-294-6172
www.brovennatrading.example
Look and feel

```html
<!DOCTYPE html>
<html lang="en">
<head>
<meta charset="utf-8">
<title>Brovenna Trading/Shipping – Business Card</title>
<link rel="stylesheet" href="https://fonts.googleapis.com/css2?family=Marcellus+SC&display=swap">
<style>
  :root {
    --backdrop: #e4e4e2;
    --paper: #fbfbf9;
    --paper-shade: #f1f1ee;
    --burgundy: #7d1c27;
    --gold: #c8902a;
    --ink: #2b2b2b;
    --ink-soft: #4a4a4a;
  }
  * { margin: 0; padding: 0; box-sizing: border-box; }
  html, body {
    width: 1200px;
    height: 1000px;
    overflow: hidden;
    background: var(--backdrop);
  }
  body {
    display: flex;
    align-items: center;
    justify-content: center;
    font-family: "Marcellus SC", "Times New Roman", serif;
  }
  .business-card {
    position: relative;
    width: 880px;
    height: 520px;
    background: radial-gradient(ellipse at 30% 20%, var(--paper) 0%, var(--paper-shade) 100%);
    box-shadow: 0 14px 36px rgba(0, 0, 0, 0.18);
  }
  .brand {
    position: absolute;
    left: 500px;
    top: 60px;
    display: flex;
    align-items: flex-end;
    gap: 18px;
  }
  .brand-square {
    width: 150px;
    height: 150px;
    background: var(--burgundy);
  }
  .brand-name {
    font-size: 34px;
    letter-spacing: 2px;
    color: var(--ink);
    line-height: 1;
  }
  .identity {
    position: absolute;
    left: 150px;
    top: 270px;
    display: flex;
    flex-direction: column;
    align-items: flex-end;
    width: 380px;
  }
  .person-name {
    font-size: 27px;
    letter-spacing: 2.5px;
    color: var(--burgundy);
    text-transform: uppercase;
    white-space: nowrap;
  }
  .person-title {
    margin-top: 10px;
    font-size: 22px;
    letter-spacing: 2px;
    color: var(--gold);
  }
  .contact-list {
    position: absolute;
    left: 150px;
    top: 368px;
    list-style: none;
    font-size: 19px;
    letter-spacing: 1.5px;
    color: var(--ink-soft);
    line-height: 28px;
  }
</style>
</head>
<body>
  <article class="business-card">
    <div class="brand">
      <div class="brand-square"></div>
      <span class="brand-name">BROVENNA</span>
    </div>

    <div class="identity">
      <h1 class="person-name">Marcus T. Hollenbrand</h1>
      <p class="person-title">CEO</p>
    </div>

    <ul class="contact-list">
      <li class="contact-phone">555-294-6172</li>
      <li class="contact-email">mark@brovennatrading.example</li>
      <li class="contact-web">www.brovennatrading.example</li>
      <li class="contact-company">Brovenna Trading/Shipping, LLC.</li>
    </ul>
  </article>
</body>
</html>
```